Northgate Roofing Works Inc Business cards

Commercial and Residential Roofing contractor needs design logo and card design. Can be single or double sided but must incorporate:
Persons Name:
Persons Title:
Mailing Address: PO Box 3719
Physical Address: 58 Fenwick Lane
Hollisford, Ma. 01593
800-316-5842
508-712-5842
Fax: 508-712-5867
Cell: Person Cell number
email address
Website: WWW.northgateroofworks.com

Target Market(s)

Residential home owners and commercial building owners

Industry/Entity Type

Roofing

Contact Information for Business Card

Persons Name:
Persons Title:
Hollisford, Ma. 01593
800-316-5842
508-712-5842
Fax: 508-712-5867
Cell: Person Cell number
email address

Logo Text

Large enough to service small enough to care

Font styles to use
Serif

Colors
0355a3

Requirements
Must have
• Commercial and Residential Roofing contractor needs design logo and card design. Can be single or double sided but must incorporate:
• Persons Name:
• Persons Title:
• Mailing Address: PO Box 3719
• Physical Address: 58 Fenwick Lane
• Hollisford, Ma. 01593
• 800-316-5842
• 508-712-5842
• Fax: 508-712-5867
• Cell: Person Cell number
• email address
• Website: WWW.northgateroofworks.com
Nice to have
• ..
Should not have
• I'm looking for something different. I have had the same card for 23 years. I attached what both sides of my present card looks like.

```html
<!DOCTYPE html>
<html lang="en">
<head>
<meta charset="utf-8">
<title>Northgate Roofing Works Inc — Business Cards</title>
<link rel="stylesheet" href="https://fonts.googleapis.com/css2?family=Tinos:wght@400;700&display=swap">
<style>
  :root {
    --backdrop: #2b2b2b;
    --card: #ffffff;
    --brand-red: #7b1b15;
    --ink: #141414;
    --rule: #1e1e1e;
    --band-text: #ffffff;
  }
  * { margin: 0; padding: 0; box-sizing: border-box; }
  html, body { width: 1200px; height: 900px; overflow: hidden; }
  body {
    background: var(--backdrop);
    font-family: "Tinos", "Times New Roman", serif;
    color: var(--ink);
    position: relative;
  }
  .card {
    position: absolute;
    left: 296px;
    width: 608px;
    background: var(--card);
    overflow: hidden;
  }
  .card--front { top: 73px; height: 357px; }
  .card--back { top: 472px; height: 355px; }

  .wordmark { position: absolute; text-align: right; }
  .wordmark__tagline {
    color: var(--brand-red);
    font-weight: 700;
    font-size: 11px;
    line-height: 1;
    white-space: nowrap;
  }
  .wordmark__name {
    font-weight: 700;
    color: var(--ink);
    white-space: nowrap;
    line-height: 1;
  }
  .card--front .wordmark { right: 46px; top: 63px; }
  .card--front .wordmark__name { font-size: 26px; margin-top: 8px; }
  .card--back .wordmark { left: 111px; top: 158px; }
  .card--back .wordmark__tagline { font-size: 11.5px; }
  .card--back .wordmark__name { font-size: 29px; margin-top: 9px; }

  .person { position: absolute; left: 42px; top: 166px; right: 41px; }
  .person__name { font-size: 22px; font-weight: 700; line-height: 1; }
  .person__title-row { display: flex; align-items: flex-end; margin-top: 5px; }
  .person__title { color: var(--brand-red); font-size: 14px; line-height: 1; }
  .person__rule { flex: 1; height: 1px; background: var(--rule); margin-left: 10px; margin-bottom: 2px; }

  .contact-list { position: absolute; list-style: none; font-size: 15px; }
  .contact-list li { display: flex; align-items: center; height: 18.5px; white-space: nowrap; }
  .contact-list svg { width: 12px; height: 12px; margin-right: 10px; flex: none; }
  .contact-list--phones { left: 43px; top: 221px; }
  .contact-list--online { left: 374px; top: 221px; }

  .band { position: absolute; bottom: 0; }
  .band svg { display: block; }
  .band__text {
    position: absolute; inset: 0;
    display: flex; align-items: center; justify-content: center;
    color: var(--band-text);
    white-space: nowrap;
  }
  .band--address { left: 100px; width: 408px; height: 36px; }
  .band--address .band__text { font-size: 13px; }
  .band--web { right: 0; width: 268px; height: 41px; }
  .band--web .band__text { font-size: 15px; font-weight: 700; padding-left: 40px; justify-content: flex-start; }
</style>
</head>
<body>

<section class="card card--front" aria-label="Business card front">
  <div class="wordmark">
    <p class="wordmark__tagline">Built Strong For Every Roof and Close Enough To Care</p>
    <p class="wordmark__name">Northgate Roofing Works Inc</p>
  </div>

  <div class="person">
    <p class="person__name">Daniel Whitcomb</p>
    <div class="person__title-row">
      <p class="person__title">Manager</p>
      <span class="person__rule"></span>
    </div>
  </div>

  <ul class="contact-list contact-list--phones">
    <li><svg viewBox="0 0 12 12"><rect width="12" height="12" rx="2" fill="#7b1b15"/><path d="M3 2.5l1.6 0 .6 2-1 .8a5 5 0 0 0 2.5 2.5l.8-1 2 .6v1.6c-3.5.3-6.8-3-6.5-6.5z" fill="#fff"/></svg>800-316-5842</li>
    <li><svg viewBox="0 0 12 12"><rect width="12" height="12" rx="2" fill="#7b1b15"/><path d="M3 2.5l1.6 0 .6 2-1 .8a5 5 0 0 0 2.5 2.5l.8-1 2 .6v1.6c-3.5.3-6.8-3-6.5-6.5z" fill="#fff"/></svg>508-712-5842</li>
    <li><svg viewBox="0 0 12 12"><rect width="12" height="12" rx="2" fill="#7b1b15"/><rect x="2.5" y="3" width="7" height="5" fill="none" stroke="#fff"/><rect x="4" y="8" width="4" height="1.5" fill="#fff"/></svg>508-712-5867</li>
    <li><svg viewBox="0 0 12 12"><rect width="12" height="12" rx="2" fill="#7b1b15"/><rect x="3.5" y="2" width="5" height="8" rx="1" fill="none" stroke="#fff"/></svg>508-712-4093</li>
  </ul>

  <ul class="contact-list contact-list--online">
    <li><svg viewBox="0 0 12 12"><rect width="12" height="12" rx="2" fill="#7b1b15"/><rect x="2.5" y="3.5" width="7" height="5" fill="none" stroke="#fff"/><path d="M2.5 3.5l3.5 3 3.5-3" fill="none" stroke="#fff"/></svg>info@northgateroof.com</li>
    <li><svg viewBox="0 0 12 12"><rect width="12" height="12" rx="2" fill="#7b1b15"/><rect x="2.5" y="2.5" width="7" height="5.5" fill="none" stroke="#fff"/><rect x="4" y="8.5" width="4" height="1" fill="#fff"/></svg>www.northgateroofworks.com</li>
  </ul>

  <div class="band band--address">
    <svg width="408" height="36" viewBox="0 0 408 36"><polygon points="24,0 372,0 408,36 0,36" fill="#7b1b15"/></svg>
    <p class="band__text">PO Box 3719, 58 Fenwick Lane, Hollisford, Ma. 01593</p>
  </div>
</section>

<section class="card card--back" aria-label="Business card back">
  <div class="wordmark">
    <p class="wordmark__tagline">Built Strong For Every Roof and Close Enough To Care</p>
    <p class="wordmark__name">Northgate Roofing Works Inc</p>
  </div>

  <div class="band band--web">
    <svg width="268" height="41" viewBox="0 0 268 41"><polygon points="32,0 268,0 268,41 0,41" fill="#7b1b15"/></svg>
    <p class="band__text">www.northgateroofworks.com</p>
  </div>
</section>

</body>
</html>
```